Website Homepage for Gulfward Crest Labs

Website is a white label new branding of this product:
https://www.roofbrightly.example

Looking for home page / landing page design.

The focus should be on its characteristics that showcase its ability to protect your roof from hurricanes and weather. Focus is only on the roof use case.

Helps restore original color
Bonds shingle granules
Penetrates and rejuvenates
Extend your roofs life
Prevents mold, mildew and moss growth
FrostVeil Colors are heat reflective and UV resistance
Environmentally Friendly
Added flexibility
Added Impact Resistance
Added Wind Resistance
Heat reflective
Reflect harmful UV rays
Reduce energy consumption
Extend the life of the shingle
Stop mold, mildew and algae from growing again!
Built it mildicide, moldicide, and algaecide.

Some other consideration marketing ideas to portray:

Roof replacement alternative with $0 down financing

Don’t replace, rejuvenate!

Stop! Before replacing your roof look at this solution…. With our advanced technology spray and seal coatings you can have a rejuvenated roof that is better than a new one! At a fraction of the cost!

Repel wind, repel water and repel impact. Make your roof stronger than ever.

Is your roof ready for hurricane season? What if there was a simple 1 day application coating that could help you to strengthen your roof against wind, rain and impact?

Self insured home? Protect your roof with our rejuvenating roof coatings that extend the life of your roof by 15+ years.

Have you recently installed a roof? Don’t wait for the next hurricane to damage it. Protect it today with our sealant coatings that repel wind, water and impact!

Ready for a new roof but don’t have the budget. Use our colored coatings that not only make your roof new again, but can also recolor it!

The sun is damaging your roof every day! Our coatings protect it from UV damage as well as water, wind, and impact!

Have a tile or clay roof? Tired of algae, mold and mildew growing on your roof? We will clean your roof and prevent regrowth in the future with our coatings!

Industry/Entity Type

Construction

Number of Pages Required

1 page

Font styles to use
Sans Serif

Colors
0054AA
0677BA
7BADD7
CADEEF
E8F1F8
0094D4
00A9DD
6FCCEA
C7EBF8
E9F6FB

Requirements
Nice to have
• Modern blue / grey / black color scheme. Not a lot of white space.

```html
<!DOCTYPE html>
<html lang="en">
<head>
<meta charset="utf-8">
<title>Gulfward Crest Labs — Roof Protection Coatings</title>
<link href="https://fonts.googleapis.com/css2?family=Poppins:wght@400;500;600;700&display=swap" rel="stylesheet">
<style>
:root{
  --blue:#1a8fe3;
  --blue-bright:#2196ee;
  --navy:#16325e;
  --navy-deep:#0f2f5c;
  --topbar:#0c2748;
  --ink:#1b1b1b;
  --muted:#6b6f76;
  --field:#ececec;
  --footer:#0d0d0f;
  --white:#ffffff;
}
*{box-sizing:border-box;margin:0;padding:0}
html,body{width:1200px;height:5054px;overflow:hidden}
body{position:relative;font-family:"Poppins",sans-serif;color:var(--ink);background:var(--white)}
.abs{position:absolute}
.btn{position:absolute;display:flex;align-items:center;justify-content:center;background:var(--blue);color:var(--white);font-size:17px;font-weight:500;letter-spacing:.3px}
.h2{position:absolute;color:var(--navy);font-weight:600;font-size:26px;line-height:34px;text-transform:uppercase}

.topbar{left:0;top:0;width:1200px;height:35px;background:var(--topbar);color:var(--white);font-size:13px;display:flex;align-items:center;gap:48px;padding-left:34px}
.topbar span{display:flex;align-items:center;gap:8px}

.nav{left:0;top:35px;width:1200px;height:80px;background:var(--white)}
.logo{display:flex;align-items:center;gap:10px;font-weight:700;color:var(--navy);font-size:19px;line-height:22px}
.logo i{width:26px;height:26px;background:var(--navy);border-radius:50%;display:block;flex:none}
.menu{position:absolute;top:32px;font-size:17px;font-weight:500;color:var(--ink)}

.hero{left:0;top:115px;width:1200px;height:565px;background:linear-gradient(160deg,#5d6f60 0%,#46554a 45%,#3a4640 100%)}
.hero-shade{left:0;top:115px;width:1200px;height:565px;background:rgba(10,22,38,.45)}
.hero-title{left:34px;top:258px;width:560px;color:var(--white);font-size:35px;line-height:43px;font-weight:700;text-transform:uppercase}
.hero-sub{left:38px;top:352px;width:505px;color:var(--white);font-size:12px;line-height:22px;text-transform:uppercase}
.play{left:858px;top:272px;width:94px;height:94px;border-radius:50%;background:var(--blue);border:6px solid rgba(255,255,255,.35)}

.form-card{left:652px;top:424px;width:491px;height:604px;background:var(--white);box-shadow:0 18px 40px rgba(0,0,0,.14)}
.form-card h3{position:absolute;left:0;top:40px;width:100%;text-align:center;color:var(--navy);font-size:25px;font-weight:600}
.field{position:absolute;height:36px;background:var(--field);border-bottom:2px solid #c9c9c9;font-size:10.5px;color:#9a9a9a;padding:14px 0 0 14px;text-transform:uppercase}

.feat{position:absolute;top:832px;width:140px;text-align:center;font-size:17px;color:var(--ink)}
.feat svg{display:block;margin:0 auto 12px}

.photo{position:absolute}
.badge{left:378px;top:1450px;width:190px;height:190px;border-radius:50%;background:var(--blue);color:var(--white);text-align:center}
.badge b{display:block;font-size:62px;line-height:62px;margin-top:40px;font-weight:600}
.badge span{display:block;font-size:16px;line-height:20px}
.about-p{left:645px;top:1330px;width:480px;font-size:14px;line-height:20px;color:var(--muted)}

.band{left:0;top:1775px;width:1200px;height:818px;background:linear-gradient(180deg,#1b4a7e,#123a68)}
.band-title{left:0;top:1872px;width:1200px;text-align:center;color:var(--white);font-size:26px;line-height:34px;font-weight:600;text-transform:uppercase}
.benefit{position:absolute;width:220px;text-align:center;color:var(--white);font-size:17px;line-height:24px}
.benefit .dot{width:96px;height:96px;border-radius:50%;background:var(--blue-bright);margin:0 auto 22px;display:flex;align-items:center;justify-content:center}
.btn-outline{background:var(--blue);border:3px solid var(--white)}

.cta-photo{left:14px;top:3463px;width:1186px;height:289px;background:linear-gradient(120deg,#4b6e4f,#5f7f5a 40%,#3f5a45)}
.cta-text{left:62px;top:3530px;color:var(--white)}
.cta-text h2{font-size:29px;font-weight:600;text-transform:uppercase}
.cta-text p{font-size:19px;line-height:26px;margin-top:8px;width:470px}

.quote{position:absolute;top:3965px;width:330px;height:175px;background:var(--white);box-shadow:0 8px 30px rgba(0,0,0,.08);padding:32px 30px;font-size:13.5px;line-height:21px;color:var(--muted)}
.person{position:absolute;top:4160px;display:flex;align-items:center;gap:18px}
.avatar{width:60px;height:60px;border-radius:50%;background:linear-gradient(135deg,#b8b2ab,#6e6864)}
.person b{display:block;color:var(--navy);font-size:15px;font-weight:600}
.person small{display:block;color:var(--blue);font-size:10px;text-transform:uppercase}

.media{position:absolute;top:4465px;height:56px;background:#c4c9cf;border-radius:6px}

.footer{left:0;top:4608px;width:1200px;height:446px;background:var(--footer)}
.fcol{position:absolute;top:4688px;font-size:15px;color:var(--white)}
.fcol h4{color:var(--blue-bright);font-size:20px;font-weight:600;text-transform:uppercase;margin-bottom:14px;white-space:nowrap}
.fcol li{list-style:none;line-height:46px;text-transform:uppercase;white-space:nowrap}
.fcol li::before{content:"›";color:var(--blue-bright);margin-right:10px}
.fline{left:44px;top:5018px;width:1140px;height:2px;background:var(--blue)}
.fbottom{top:5030px;font-size:11.5px;font-weight:600;text-transform:uppercase;color:var(--white)}
.social{width:30px;height:30px;border-radius:50%;background:var(--blue-bright);position:absolute;top:4935px}
</style>
</head>
<body>

<div class="abs topbar">
  <span><svg width="13" height="16" viewBox="0 0 12 16"><path d="M6 0a6 6 0 0 0-6 6c0 4.5 6 10 6 10s6-5.5 6-10a6 6 0 0 0-6-6zm0 8.3A2.3 2.3 0 1 1 6 3.7a2.3 2.3 0 0 1 0 4.6z" fill="#4aa8f0"/></svg>742 Harbor Point Way, Suite 210</span>
  <span><svg width="15" height="15" viewBox="0 0 16 16"><path d="M3.6 1l2.4 3.2-1.5 1.7a9 9 0 0 0 5.6 5.6l1.7-1.5L15 12.4 13.4 15C6.8 14.8 1.2 9.2 1 2.6z" fill="#4aa8f0"/></svg>(800) 555-0142</span>
</div>

<div class="abs nav">
  <div class="abs logo" style="left:24px;top:29px"><i></i>Gulfward Crest Labs</div>
  <div class="menu" style="left:287px">HOME</div>
  <div class="menu" style="left:388px">ABOUT</div>
  <div class="menu" style="left:502px">SERVICES</div>
  <div class="menu" style="left:640px">GALLERY</div>
  <div class="menu" style="left:771px">TESTIMONIALS</div>
  <div class="btn" style="left:970px;top:22px;width:193px;height:40px">GET A QUOTE</div>
</div>

<section>
  <div class="abs hero" role="img" aria-label="Technician spraying protective coating on a shingle roof"></div>
  <div class="abs hero-shade"></div>
  <h1 class="abs hero-title">Protect your roof from hurricanes and weather</h1>
  <p class="abs hero-sub">With our advanced technology spray and seal coatings you can have a rejuvenated roof that is better than a new one! At a fraction of the cost!</p>
  <div class="btn" style="left:38px;top:440px;width:194px;height:38px">GET A QUOTE</div>
  <div class="abs play"><svg width="82" height="82" viewBox="0 0 82 82"><path d="M33 24l24 17-24 17z" fill="#fff"/></svg></div>
</section>

<section>
  <h2 class="h2" style="left:62px;top:738px;width:420px">Make your roof stronger than ever.</h2>
  <div class="feat" style="left:55px">
    <svg width="100" height="100" viewBox="0 0 100 100" fill="none" stroke="#1a8fe3" stroke-width="2.5"><path d="M10 15l12 20M18 10l12 22M26 8l10 20"/><path d="M30 90l20-40h45l-20 40z"/><path d="M40 70h40M45 60h40M50 80h20" stroke="#16325e"/></svg>Repel Wind</div>
  <div class="feat" style="left:250px">
    <svg width="100" height="100" viewBox="0 0 100 100" fill="none" stroke="#1a8fe3" stroke-width="2.5"><path d="M35 25a12 12 0 0 1 24-4 9 9 0 0 1 8 13H33a7 7 0 0 1 2-9z"/><path d="M40 42v6M50 42v6M60 42v6"/><path d="M15 80l35-28 35 28M25 80v12h50V80" stroke="#16325e"/></svg>Repel Water</div>
  <div class="feat" style="left:458px">
    <svg width="100" height="100" viewBox="0 0 100 100" fill="none" stroke="#1a8fe3" stroke-width="2.5"><circle cx="34" cy="30" r="14"/><circle cx="34" cy="30" r="6"/><path d="M30 88l20-36h40l-20 36zM40 70h40M46 60h40" stroke="#16325e"/></svg>Repel Impact</div>
</section>

<div class="abs form-card">
  <h3>10% OFF ROOF PROTECTION</h3>
  <div class="field" style="left:28px;top:116px;width:206px">First Name</div>
  <div class="field" style="left:258px;top:116px;width:206px">Last Name</div>
  <div class="field" style="left:28px;top:174px;width:436px">Email Address</div>
  <div class="field" style="left:28px;top:233px;width:436px">Phone Number</div>
  <div class="field" style="left:28px;top:289px;width:436px">Address</div>
  <div class="field" style="left:28px;top:349px;width:206px">City</div>
  <div class="field" style="left:258px;top:349px;width:206px">State</div>
  <div class="field" style="left:28px;top:406px;width:436px">Project</div>
  <div class="btn" style="left:148px;top:512px;width:194px;height:40px">GET A QUOTE</div>
</div>

<section>
  <div class="photo" style="left:60px;top:1170px;width:530px;height:413px;background:linear-gradient(180deg,#9aa7b3 0%,#b9c2c9 35%,#59606a 36%,#6c7078 62%,#d9d4c8 63%,#cfc9bd 100%)" role="img" aria-label="Two-storey house with coated grey shingle roof and white garage door"></div>
  <div class="abs badge"><b>10+</b><span>Years Of<br>Experience</span></div>
  <h2 class="h2" style="left:645px;top:1222px;width:390px">Is your roof ready for hurricane season?.</h2>
  <p class="abs about-p">What if there was a simple 1 day application coating that could help you to strengthen your roof against wind, rain and impact. The sun is damaging your roof every day! Our coatings protect it from UV damage as well as water, wind, and impact!</p>
  <div class="btn" style="left:645px;top:1452px;width:195px;height:40px">MORE ABOUT US</div>
</section>

<section>
  <div class="abs band" role="img" aria-label="Dark blue tinted close-up of roof shingles"></div>
  <h2 class="abs band-title">Our coatings protect it from UV damage<br>as well as water, wind, and impact!</h2>

  <div class="benefit" style="left:133px;top:2008px"><div class="dot"><svg width="48" height="48" fill="none" stroke="#fff" stroke-width="2"><rect x="12" y="14" width="22" height="26" rx="3"/><path d="M16 14V8h14v6M34 20h6v14h-6"/></svg></div>Helps restore<br>original color</div>
  <div class="benefit" style="left:358px;top:2015px"><div class="dot"><svg width="48" height="48" fill="none" stroke="#fff" stroke-width="2"><circle cx="24" cy="24" r="5"/><path d="M24 6v10M24 32v10M6 24h10M32 24h10M11 11l7 7M30 30l7 7M37 11l-7 7M11 37l7-7"/></svg></div>Bonds shingle<br>granules</div>
  <div class="benefit" style="left:603px;top:2015px"><div class="dot"><svg width="48" height="48" fill="none" stroke="#fff" stroke-width="2"><path d="M6 30l18-16 18 16M10 26h28M14 22h20M10 30v6h28v-6"/></svg></div>Extend your<br>roofs life</div>
  <div class="benefit" style="left:860px;top:2008px"><div class="dot"><svg width="48" height="48" fill="none" stroke="#fff" stroke-width="2"><circle cx="24" cy="24" r="12"/><circle cx="20" cy="21" r="2"/><circle cx="28" cy="27" r="3"/><circle cx="8" cy="10" r="2"/><circle cx="40" cy="38" r="2"/></svg></div>Prevents mold, mildew<br>and moss growth</div>

  <div class="benefit" style="left:133px;top:2222px"><div class="dot"><svg width="48" height="48" fill="none" stroke="#fff" stroke-width="2"><circle cx="24" cy="24" r="15"/><path d="M14 16c6 2 8 8 4 12M30 12c-2 6 6 8 8 14"/></svg></div>Environmentally<br>Friendly</div>
  <div class="benefit" style="left:358px;top:2222px"><div class="dot"><svg width="48" height="48" fill="none" stroke="#fff" stroke-width="2"><circle cx="24" cy="24" r="8"/><path d="M24 6v6M24 36v6M6 24h6M36 24h6M11 11l4 4M33 33l4 4M37 11l-4 4M11 37l4-4"/></svg></div>Heat reflective</div>
  <div class="benefit" style="left:603px;top:2222px"><div class="dot"><svg width="48" height="48" fill="none" stroke="#fff" stroke-width="2"><path d="M6 18h24a5 5 0 1 0-5-5M6 26h30a5 5 0 1 1-5 5M10 34h12"/></svg></div>Added Wind<br>Resistance</div>
  <div class="benefit" style="left:860px;top:2222px"><div class="dot"><svg width="48" height="48" fill="none" stroke="#fff" stroke-width="2"><path d="M36 16a15 15 0 1 0 3 12"/><path d="M24 14v11l7 5M36 8v8h-8"/></svg></div>Extend the life of<br>the shingle</div>

  <div class="btn btn-outline" style="left:505px;top:2463px;width:195px;height:40px">VIEW MORE</div>
</section>

<section>
  <h2 class="h2" style="left:0;top:2655px;width:1200px;text-align:center">Our recent work</h2>
  <div class="photo" style="left:60px;top:2763px;width:580px;height:242px;background:linear-gradient(180deg,#a8b2ba 0%,#5c6168 40%,#ddd6c8 70%,#7e8a5a 100%)" role="img" aria-label="Coated roof on a suburban home with garage"></div>
  <div class="photo" style="left:655px;top:2763px;width:487px;height:242px;background:linear-gradient(180deg,#b4c2cc 0%,#6d8a5c 35%,#8b8e92 60%,#6f7378 100%)" role="img" aria-label="Long shingle roof with countryside behind"></div>
  <div class="photo" style="left:60px;top:3023px;width:350px;height:244px;background:linear-gradient(180deg,#7a8f66,#5d6f55 60%,#4d5f58)" role="img" aria-label="Worker in safety harness on roof"></div>
  <div class="photo" style="left:427px;top:3023px;width:350px;height:244px;background:linear-gradient(160deg,#a7937a,#7a756f 50%,#8d8a86)" role="img" aria-label="Technician spraying coating on shingles"></div>
  <div class="photo" style="left:793px;top:3023px;width:349px;height:244px;background:linear-gradient(180deg,#5a7a5a 0%,#6f8a6a 40%,#8a8a8c 60%,#707274)" role="img" aria-label="Technician applying coating near evergreen trees"></div>
  <div class="btn" style="left:512px;top:3333px;width:191px;height:37px">VIEW GALLERY</div>
</section>

<section>
  <div class="abs cta-photo" role="img" aria-label="Technician spraying a roof with farmland behind"></div>
  <svg class="abs" style="left:14px;top:3463px" width="622" height="289"><polygon points="0,0 622,0 506,289 0,289" fill="#2196ee"/></svg>
  <div class="abs cta-text">
    <h2>Have a tile or clay roof?</h2>
    <p>We will clean your roof and prevent regrowth in the future with our coatings!</p>
  </div>
  <div class="btn" style="left:62px;top:3655px;width:213px;height:42px;background:var(--navy-deep);font-size:19px">GET A QUOTE</div>
</section>

<section>
  <h2 class="h2" style="left:0;top:3850px;width:1200px;text-align:center;font-size:28px">What customer say’s</h2>
  <div class="quote" style="left:75px">Egestas fringilla phasellus faucibus scelerisque. Massa tincidunt dui ut ornare lectus. Elit ullamcorper dignissim cras tincidunt lobortis feugiat vivamus at.</div>
  <div class="quote" style="left:442px">Egestas fringilla phasellus faucibus scelerisque. Massa tincidunt dui ut ornare lectus. Elit ullamcorper dignissim cras tincidunt lobortis feugiat vivamus at.</div>
  <div class="quote" style="left:812px">Egestas fringilla phasellus faucibus scelerisque. Massa tincidunt dui ut ornare lectus. Elit ullamcorper dignissim cras tincidunt lobortis feugiat vivamus at.</div>
  <div class="person" style="left:100px"><div class="avatar" role="img" aria-label="Customer portrait"></div><div><b>Dana R. Whitfield</b><small>Customer</small></div></div>
  <div class="person" style="left:466px"><div class="avatar" role="img" aria-label="Customer portrait"></div><div><b>Dana R. Whitfield</b><small>Customer</small></div></div>
  <div class="person" style="left:846px"><div class="avatar" role="img" aria-label="Customer portrait"></div><div><b>Dana R. Whitfield</b><small>Customer</small></div></div>
</section>

<section>
  <h2 class="h2" style="left:0;top:4366px;width:1200px;text-align:center">As seen on?</h2>
  <div class="media" style="left:68px;width:175px"></div>
  <div class="media" style="left:298px;width:168px;top:4452px;height:78px"></div>
  <div class="media" style="left:520px;width:172px"></div>
  <div class="media" style="left:745px;width:170px;top:4452px;height:72px"></div>
  <div class="media" style="left:970px;width:166px;top:4475px;height:36px"></div>
</section>

<footer>
  <div class="abs footer"></div>
  <div class="abs logo" style="left:66px;top:4712px;color:#fff"><i style="background:#fff"></i>Gulfward Crest Labs</div>
  <div class="abs" style="left:62px;top:4798px;color:#fff;font-size:15px;display:flex;gap:14px;align-items:center"><svg width="22" height="22" viewBox="0 0 16 16"><path d="M3.6 1l2.4 3.2-1.5 1.7a9 9 0 0 0 5.6 5.6l1.7-1.5L15 12.4 13.4 15C6.8 14.8 1.2 9.2 1 2.6z" fill="#2196ee"/></svg>(800) 555-0142</div>
  <div class="abs" style="left:62px;top:4836px;color:#fff;font-size:15px;line-height:19px;display:flex;gap:14px"><svg width="20" height="26" viewBox="0 0 12 16"><path d="M6 0a6 6 0 0 0-6 6c0 4.5 6 10 6 10s6-5.5 6-10a6 6 0 0 0-6-6zm0 8.3A2.3 2.3 0 1 1 6 3.7a2.3 2.3 0 0 1 0 4.6z" fill="#2196ee"/></svg><span>742 Harbor Point Way,<br>Suite 210 Tampa, Florida<br>33602 United States</span></div>
  <div class="social" style="left:90px"></div>
  <div class="social" style="left:140px"></div>
  <div class="social" style="left:190px"></div>

  <div class="fcol" style="left:378px"><h4>Sealers</h4><ul><li>Roof Sealers</li><li>Roof Coatings</li><li>Energy Efficient Roof</li><li>Roof Facts</li></ul></div>
  <div class="fcol" style="left:683px"><h4>Company</h4><ul><li>Home</li><li>About</li><li>Gallery</li><li>Contact</li></ul></div>
  <div class="fcol" style="left:910px"><h4 style="font-size:18px">Gulfward Crest Labs</h4><ul><li>FAQs</li><li>Test Videos</li><li>Video Gallery</li><li>Get A Quote</li></ul></div>

  <div class="abs fline"></div>
  <div class="abs fbottom" style="left:44px">© All rights reserved by Gulfward Crest Labs</div>
  <div class="abs fbottom" style="right:16px">Privacy Policy | Term and Conditions</div>
</footer>

</body>
</html>
```